Notes nobody handed you at college

Notes nobody handed you at college

"Unfiltered tips to help early career professionals successfully navigate the workplace"

I'VE INCLUDED LINKS TO SOME EXAMPLES OF COVERS THAT I LIKE.

Open to a creative concept. The book is sort of a guide for early career professionals and how they should navigate corporate America. Inside the book, I am giving tips on how to navigate work life. Most executive professionals have coaches, advisors and mentors to help them navigate the stressors of work. This is sort of a playbook for young professionals in the workplace.

Book Dimensions: 5.5" X 8.5"

Brightward Shift
https://www.plorvane.example/Brightward-Shift-Locating-Growing-Pleasing-ebook/dp/K47Q22TR8M/ref=sr_1_1?ie=UTF8&qid=1500000000&sr=8-1&keywords=brightward+shift

The Compass Ledger: Chart Your Calling. Outgrow Your Dread of Missteps. Apply Your Inborn Gifts And Abilities To Shape A Rewarding Path. https://www.plorvane.example/Compass-Ledger-Calling-Abilities-Rewarding-ebook/dp/K83W51LP0D/ref=pd_sim_351_11?_encoding=UTF8&psc=1&refRID=QTRA4KMWZBL2HDYC70XE

Cubicle Exit Route: Nine Moves to Launch a Kitchen-Table Venture, Leave the Office and Savor the Liberty: Features Talks with Warren Ode Hasket, Lyle Brantic, Gus Merrowby, Dale Finchum, Teodor Vasquill & more!
https://www.plorvane.example/Cubicle-Exit-Route-Talks-Vasquill-ebook/dp/K26H90YS44/ref=pd_sim_351_20?_encoding=UTF8&psc=1&refRID=LMPE3QDKWRZGB81VNTHA

The Quick Draft Calendar: The Lone Founder’s Handbook to Twelve Months of Article Topics in an Afternoon and Writing Pieces That Grip and Persuade
https://www.plorvane.example/Quick-Draft-Calendar-Founders-ebook/dp/K59F13BX7N/ref=pd_sim_351_4_encoding=UTF8&psc=1&refRID=GDUY46PKRJ0SMVCT2EQW

Crafting a Magnetic Landing Screen in Nine Easy Moves: Your Map to Storefront Landing Copy that Turns Browsers into Prospects & Buyers (Crafting Series... Volume 3)
https://www.plorvane.example/Crafting-Magnetic-Landing-Easy-Moves-ebook/dp/K38N67VC2J/ref=pd_sim_351_1?_encoding=UTF8&psc=1&refRID=RSOB45TQXFYMUHIKWDLE

Target Market(s)

College Students- Early Career Professionals

Industry/Entity Type

School

Font styles to use
Serif

Colors

Designer to choose colors to be used in the design.

Requirements
Must have
• Diversity in the cover- something eye catching. Photo on back cover. I'VE INCLUDED LINKS TO SOME EXAMPLES OF COVERS THAT I LIKE
Nice to have
• Designers have the flexibility to exert their creativity.I'VE INCLUDED LINKS TO SOME EXAMPLES OF COVERS THAT I LIKE
Should not have
• My picture on the cover

```html
<!DOCTYPE html>
<html lang="en">
<head>
<meta charset="utf-8">
<title>Notes Nobody Handed You at College – Cover Set</title>
<link rel="stylesheet" href="https://fonts.googleapis.com/css2?family=Bebas+Neue&family=Special+Elite&family=Open+Sans:wght@400;600&family=Nothing+You+Could+Do&display=swap">
<style>
  :root {
    --stage: #9b9b9b;
    --blue-deep: #1f86ee;
    --blue-mid: #4aa3f2;
    --blue-light: #bfe0fb;
    --white: #ffffff;
    --ink: #1a1a1a;
    --ink-soft: #2b3440;
    --label: #3a3a3a;
    --note-pink: #f3d8ec;
    --note-green: #dcecd6;
    --note-yellow: #f6f2b4;
    --photo-pink: #f2d4ea;
    --tape: #d9cfc4;
  }
  * { box-sizing: border-box; margin: 0; padding: 0; }
  html, body { width: 1200px; height: 900px; overflow: hidden; background: var(--stage); }
  .stage { position: relative; width: 1200px; height: 900px; }

  .cover {
    position: absolute; top: 50px; width: 466px; height: 720px; overflow: hidden;
    background: radial-gradient(ellipse at 50% 55%, var(--blue-light) 0%, var(--blue-mid) 55%, var(--blue-deep) 100%);
    box-shadow: 0 10px 24px rgba(0,0,0,.25);
  }
  .cover--back { left: 110px; }
  .cover--front { left: 624px; }
  .cover__frame { position: absolute; inset: 12px; border: 4px solid var(--white); pointer-events: none; }

  .cover-label {
    position: absolute; top: 790px; width: 466px; text-align: center;
    font-family: "Open Sans", sans-serif; font-size: 40px; color: var(--label);
  }
  .cover-label--back { left: 110px; }
  .cover-label--front { left: 624px; }

  .dash-path { position: absolute; inset: 0; width: 100%; height: 100%; }

  .sticky {
    position: absolute; box-shadow: 3px 5px 10px rgba(0,0,0,.25);
    font-family: "Nothing You Could Do", cursive; color: var(--ink);
    display: flex; align-items: center; justify-content: center; text-align: center;
    line-height: 1.3; padding: 12px;
  }
  .sticky--pink { background: var(--note-pink); }
  .sticky--green { background: var(--note-green); }
  .sticky--yellow { background: var(--note-yellow); }

  /* Front cover */
  .title-brackets { position: absolute; left: 0; top: 0; width: 466px; height: 260px; }
  .title { position: absolute; left: 34px; top: 40px; width: 400px; color: var(--white);
    font-family: "Bebas Neue", sans-serif; font-weight: 400; text-shadow: 2px 3px 4px rgba(0,0,0,.35); }
  .title__row { display: flex; align-items: center; gap: 8px; line-height: .85; }
  .title__row--second { margin-top: 4px; }
  .title__big { font-size: 104px; }
  .title__stack { display: flex; flex-direction: column; font-size: 40px; line-height: .95; }
  .subtitle {
    position: absolute; left: 30px; top: 265px; width: 406px; text-align: center;
    font-family: "Special Elite", serif; font-size: 12.5px; line-height: 1.35; color: var(--ink-soft);
    text-transform: uppercase;
  }
  .subtitle-rule { position: absolute; left: 40px; top: 310px; width: 386px; height: 2px;
    background: linear-gradient(90deg, transparent, rgba(255,255,255,.9), transparent); }
  .author-name {
    position: absolute; font-family: "Special Elite", serif; font-size: 16px; color: var(--ink-soft);
    letter-spacing: .5px; white-space: nowrap;
  }
  .grid-decor { position: absolute; background: rgba(255,255,255,.55); }

  /* Back cover */
  .blurb {
    position: absolute; left: 26px; top: 30px; width: 286px; height: 370px; background: var(--white);
    transform: rotate(4deg); box-shadow: 3px 6px 12px rgba(0,0,0,.25); padding: 28px 22px;
    font-family: "Special Elite", serif; color: var(--ink); text-align: center;
  }
  .blurb__heading { font-size: 24px; font-weight: 400; margin-bottom: 12px; text-align: left; padding-left: 20px; }
  .blurb__text { font-size: 11.5px; line-height: 1.32; margin-bottom: 12px; }
  .author-photo {
    position: absolute; left: 280px; top: 300px; width: 200px; height: 225px;
    background: radial-gradient(ellipse at 55% 45%, #fbe9f5 0%, var(--photo-pink) 45%, #c27a55 72%, #2a2a2e 100%);
    transform: rotate(3deg); box-shadow: 3px 6px 12px rgba(0,0,0,.25);
  }
  .about {
    position: absolute; left: 30px; top: 566px; width: 410px; height: 132px; background: var(--white);
    transform: rotate(-3deg); box-shadow: 3px 6px 12px rgba(0,0,0,.25); padding: 14px 18px;
    font-family: "Open Sans", sans-serif; color: var(--ink); overflow: hidden;
  }
  .about__heading { font-size: 12.5px; font-weight: 600; margin-bottom: 3px; }
  .about__text { font-size: 9.5px; line-height: 1.25; margin-bottom: 4px; }
  .tape { position: absolute; left: 180px; top: 552px; width: 100px; height: 26px; background: var(--tape);
    opacity: .85; transform: rotate(-2deg); }
</style>
</head>
<body>
<main class="stage">

  <!-- Back cover -->
  <section class="cover cover--back" aria-label="Back cover">
    <svg class="dash-path" viewBox="0 0 466 720" aria-hidden="true">
      <path d="M300 150 C 350 240, 330 330, 300 380 M250 430 C 230 480, 235 520, 260 545"
            fill="none" stroke="#fff" stroke-width="4" stroke-dasharray="16 12"/>
    </svg>
    <div class="cover__frame"></div>
    <div class="sticky sticky--green" style="left:350px;top:130px;width:96px;height:104px;transform:rotate(-10deg)"></div>
    <div class="sticky sticky--yellow" style="left:70px;top:410px;width:112px;height:122px;transform:rotate(12deg)"></div>
    <article class="blurb">
      <h2 class="blurb__heading">Blurb Quote</h2>
      <p class="blurb__text">Viam sumi mo id erit. Objectioni mo de necessario crediderim. Imo terra vox alios aut lor quasi. Vim quaero aut videri pendam plures duo. Extat neque arcte re ad etiam. Ego infiniti reperero mutuatur formalem sed scribere nec vel profecto.</p>
      <p class="blurb__text">Dari ut ullo id ex enim. Nunc quum eas vos bile per hic. Cujuspiam ex instituti veritatem et obversari vereorque productus. Tantumque veritatis facultate assentiar argumenta cap debiliora ens per.</p>
    </article>
    <div class="author-photo" role="img" aria-label="Author portrait photo on a soft pink backdrop"></div>
    <p class="author-name" style="left:300px;top:532px;transform:rotate(3deg)">DANA WHITLOCK</p>
    <article class="about">
      <h3 class="about__heading">ABOUT THE AUTHOR</h3>
      <p class="about__text">De iste tunc esse illa ii actu idem. Ei penitius imaginer si supponam ad. Sentiat ac referam corpore reddere proinde de si limites. At quaerantur advertisse deprehendi se. Habendae fenestra secundum at in. Nul cum majorem sae student ultimum videtur. Inanes at loquor soleam du nega si. Delusisse clausulas eundemque quarundam tes sua conceptum nuperrime.</p>
      <p class="about__text">Ignotae hac minimum cum sentire. De at ab ignorans chimerae cogitari. Ita sola quae tius vox. Aptum nia dicam vitae ego minor extra.</p>
    </article>
    <div class="tape"></div>
  </section>

  <!-- Front cover -->
  <section class="cover cover--front" aria-label="Front cover">
    <svg class="title-brackets" viewBox="0 0 466 260" aria-hidden="true">
      <path d="M38 100 V48 H150 M300 40 H432 V110 M38 200 V238 H110 M290 238 H432 V200"
            fill="none" stroke="#fff" stroke-width="5"/>
    </svg>
    <h1 class="title">
      <span class="title__row">
        <span class="title__big">NOTES</span>
        <span class="title__stack"><span>NOBODY</span><span>HANDED</span></span>
      </span>
      <span class="title__row title__row--second">
        <span class="title__stack"><span>YOU</span><span>AT</span></span>
        <span class="title__big">COLLEGE</span>
      </span>
    </h1>
    <p class="subtitle">Unfiltered tips to help early career professionals<br>successfully navigate the workplace</p>
    <div class="subtitle-rule"></div>

    <svg class="dash-path" viewBox="0 0 466 720" aria-hidden="true">
      <path d="M80 390 C 110 330, 190 340, 230 380 C 260 400, 275 375, 285 365"
            fill="none" stroke="#fff" stroke-width="4" stroke-dasharray="16 12"/>
      <path d="M100 600 C 110 640, 150 665, 180 672 M420 520 C 410 565, 395 595, 380 610"
            fill="none" stroke="#fff" stroke-width="4" stroke-dasharray="16 12"/>
    </svg>

    <div class="grid-decor" role="img" aria-label="Graph paper corner decoration" style="left:24px;top:636px;width:80px;height:56px;transform:rotate(-20deg)"></div>
    <div class="grid-decor" role="img" aria-label="Graph paper corner decoration" style="left:408px;top:566px;width:40px;height:110px;transform:rotate(-15deg)"></div>

    <div class="sticky sticky--pink" style="left:30px;top:380px;width:160px;height:184px;transform:rotate(-8deg);font-size:20px">The future depends on what you do today!</div>
    <div class="sticky sticky--green" style="left:290px;top:330px;width:148px;height:166px;transform:rotate(3deg);font-size:18px">Overcome your fear of failure!</div>
    <div class="sticky sticky--yellow" style="left:218px;top:516px;width:156px;height:146px;transform:rotate(-4deg);font-size:17px">Opportunities don't happen, you create them!</div>

    <p class="author-name" style="left:0;width:466px;text-align:center;top:676px">DANA WHITLOCK</p>
    <div class="cover__frame"></div>
  </section>

  <p class="cover-label cover-label--back">Back</p>
  <p class="cover-label cover-label--front">Front</p>
</main>
</body>
</html>
```